A5 Magazine Cover Design

I need a front cover designing for a new community magazine called BELVOR. BELVOR will be listing local buisnesses and local interest articles for the residents in my area. I need the look to be clean but inviting.

I will consider any colour combination as long as its not too bright.

```html
<!DOCTYPE html>
<html lang="en">
<head>
<meta charset="utf-8">
<title>BELVOR – cover series</title>
<link rel="stylesheet" href="https://fonts.googleapis.com/css2?family=Fira+Sans:ital,wght@0,500;0,600;1,700&display=swap">
<style>
  :root {
    --page-top: #ffffff;
    --page-bottom: #c6c7c9;
    --white: #ffffff;
    --panel-dark: #141414;
    --oct: #f0a872;
    --nov: #b2d143;
    --dec: #b997be;
    --jan: #00a05a;
    --photo-dark: #1f2a14;
    --photo-leaf: #5d7a2c;
    --photo-light: #9bb14e;
  }
  * { margin: 0; padding: 0; box-sizing: border-box; }
  html, body {
    width: 1200px; height: 899px; overflow: hidden;
  }
  body {
    position: relative;
    background: linear-gradient(to bottom, var(--page-top) 0%, var(--page-top) 64%, var(--page-bottom) 100%);
    font-family: "Fira Sans", sans-serif;
  }
  .cover {
    position: absolute; left: 128px; top: 48px;
    width: 520px; height: 790px;
    background: var(--tone);
    transform-origin: 50% 50%;
  }
  .cover--oct { --tone: var(--oct); }
  .cover--nov { --tone: var(--nov); transform: translate(150px, 0) rotate(5deg); }
  .cover--dec { --tone: var(--dec); transform: translate(305px, 18px) rotate(9.3deg); }
  .cover--jan { --tone: var(--jan); transform: translate(452px, 6px) rotate(15deg); }

  .masthead {
    position: absolute; left: 40px; right: 40px; top: 22px;
    color: var(--white);
  }
  .masthead-name {
    font-weight: 600; font-size: 96px; line-height: 100px;
    letter-spacing: 1px;
  }
  .masthead-tagline {
    margin-top: 12px;
    text-align: right;
    font-weight: 500; font-size: 25px; line-height: 30px;
  }
  .cover-photo {
    position: absolute; left: 0; top: 200px;
    width: 440px; height: 500px;
    border-radius: 0 20px 20px 0;
    background: var(--panel-dark);
  }
  .cover--oct .cover-photo {
    background:
      radial-gradient(ellipse 60% 40% at 60% 65%, var(--photo-light), transparent 70%),
      radial-gradient(ellipse 70% 50% at 30% 30%, var(--photo-leaf), transparent 75%),
      var(--photo-dark);
  }
  .feature {
    position: absolute; left: 44px; top: 578px;
    color: var(--white); font-style: italic; font-weight: 700;
  }
  .feature-title { font-size: 26px; line-height: 30px; }
  .feature-strap { font-size: 19px; line-height: 24px; }
  .feature-page { font-size: 12px; line-height: 16px; }
  .strapline {
    position: absolute; left: 46px; top: 733px;
    color: var(--white); font-weight: 600; font-size: 14px;
    line-height: 20px; white-space: nowrap;
  }
  .issue-date {
    position: absolute; left: 408px; top: 726px;
    width: 112px; height: 34px;
    border-radius: 17px 0 0 17px;
    background: var(--white);
    color: var(--tone); font-weight: 500; font-size: 15px;
    line-height: 34px; padding-left: 12px;
  }
</style>
</head>
<body>
<main class="series">

  <section class="cover cover--jan" aria-label="January 2011 issue">
    <header class="masthead">
      <p class="masthead-name">BELVOR</p>
      <p class="masthead-tagline">Local thinking</p>
    </header>
    <div class="cover-photo"></div>
    <p class="issue-date">Jan 2011</p>
  </section>

  <section class="cover cover--dec" aria-label="December 2010 issue">
    <header class="masthead">
      <p class="masthead-name">BELVOR</p>
      <p class="masthead-tagline">Local thinking</p>
    </header>
    <div class="cover-photo"></div>
    <p class="issue-date">Dec 2010</p>
  </section>

  <section class="cover cover--nov" aria-label="November 2010 issue">
    <header class="masthead">
      <p class="masthead-name">BELVOR</p>
      <p class="masthead-tagline">Local thinking</p>
    </header>
    <div class="cover-photo"></div>
    <p class="issue-date">Nov 2010</p>
  </section>

  <section class="cover cover--oct" aria-label="October 2010 issue">
    <header class="masthead">
      <p class="masthead-name">BELVOR</p>
      <p class="masthead-tagline">Local thinking</p>
    </header>
    <div class="cover-photo" role="img" aria-label="Photograph of white wild roses with yellow centres among green leaves"></div>
    <div class="feature">
      <p class="feature-title">Feature Item</p>
      <p class="feature-strap">Sub-feature strapline</p>
      <p class="feature-page">Page 4</p>
    </div>
    <p class="strapline">BELVOR searches, reviews and recommends locally</p>
    <p class="issue-date">Oct 2010</p>
  </section>

</main>
</body>
</html>
```